Advertising company unique advertising platform

we need a logo design for a new company based in Australia Melbourne. We develop innovated advertising platform where consumer can use this platform to get regular discount, as business owner they can use this platform for free advertisement. Payment for this advertisement platform only payable every two weeks, when I generate revenue for their business

Industry/Entity Type

Advertising

Contact Information for Business Card

Dale Pruitt | Co-Founder |Managing Director
Suite 718 263 Harrowgate Row Melbourne Vic 3000

ABN 41 902 615 273
Tel: +61 0491 528 307 | Email: dale.pruitt@corvelaxtro.com

Font styles to use
Decorative
Script

Requirements
Must have
• Try few different design and some round corner business card
Should not have
• One round corner business card...try 4 different colour background not only black, make sure two side is designed. Be creative so imagine you are giving this to a client make sure has wow factor, if you can also try one design with engrave like all the logo, words look 3d feel
• The word Advertising Platform use attached file font

```html
<!DOCTYPE html>
<html lang="en">
<head>
<meta charset="utf-8">
<title>Dale Pruitt – Business Card</title>
<link rel="stylesheet" href="https://fonts.googleapis.com/css2?family=Arimo:wght@400;700&display=swap">
<style>
  :root {
    --card-light: #cbcbcb;
    --card-mid: #bdbdbd;
    --card-dark: #b0b0b0;
    --frame: #121212;
    --ink: #1d1a1a;
    --brand-grey: #8c8c8c;
  }
  html, body {
    margin: 0;
    padding: 0;
    width: 1200px;
    height: 744px;
    overflow: hidden;
    background: #ffffff;
  }
  .card {
    position: relative;
    width: 1200px;
    height: 744px;
    overflow: hidden;
    font-family: "Arimo", Arial, sans-serif;
    color: var(--ink);
  }
  .card-surface {
    position: absolute;
    inset: 0;
    background: linear-gradient(135deg, var(--card-light) 0%, var(--card-mid) 50%, var(--card-dark) 100%);
  }
  .card-frame {
    position: absolute;
    inset: 0;
  }
  .holder-name {
    position: absolute;
    left: 0;
    width: 1142px;
    top: 92px;
    margin: 0;
    text-align: center;
    font-weight: 700;
    font-size: 80px;
    line-height: 1;
    letter-spacing: 0.5px;
  }
  .holder-role {
    position: absolute;
    left: 0;
    width: 1136px;
    top: 190px;
    margin: 0;
    text-align: center;
    font-size: 20px;
    line-height: 1;
  }
  .holder-address {
    position: absolute;
    left: 0;
    width: 1166px;
    top: 216px;
    margin: 0;
    text-align: center;
    font-size: 17.5px;
    line-height: 1;
    text-transform: uppercase;
  }
  .brand {
    position: absolute;
    left: 70px;
    top: 350px;
    display: flex;
    align-items: center;
    gap: 24px;
  }
  .brand-dot {
    width: 140px;
    height: 140px;
    border-radius: 50%;
    background: var(--brand-grey);
  }
  .brand-name {
    font-weight: 700;
    font-size: 48px;
    color: var(--brand-grey);
    letter-spacing: 1px;
    text-transform: uppercase;
    white-space: nowrap;
  }
  .contact {
    position: absolute;
    left: 717px;
    top: 431px;
    font-size: 17.5px;
    line-height: 24px;
  }
  .contact-abn span + span { margin-left: 26px; }
  .contact-row {
    display: flex;
  }
  .contact-label {
    width: 80px;
    text-align: right;
  }
  .contact-divider {
    width: 1px;
    margin: 0 18px 0 12px;
    background: var(--ink);
  }
</style>
</head>
<body>
<main class="card">
  <div class="card-surface" role="img" aria-label="Textured silver card stock"></div>
  <svg class="card-frame" width="1200" height="744" viewBox="0 0 1200 744" aria-hidden="true">
    <rect x="31.5" y="32.5" width="1139" height="675" rx="46" ry="46" fill="none" stroke="var(--frame)" stroke-width="27"/>
  </svg>

  <h1 class="holder-name">DALE PRUITT</h1>
  <p class="holder-role">CO-FOUNDER&nbsp; |&nbsp; MANAGING DIRECTOR</p>
  <p class="holder-address">Suite 718&nbsp;&nbsp; 263&nbsp; Harrowgate Row Melbourne Vic 3000</p>

  <div class="brand">
    <div class="brand-dot"></div>
    <div class="brand-name">Corvela Loop</div>
  </div>

  <div class="contact">
    <div class="contact-abn"><span>ABN</span><span>41&nbsp; 902&nbsp; 615&nbsp; 273</span></div>
    <div class="contact-row">
      <span class="contact-label">Tel</span>
      <span class="contact-divider"></span>
      <span class="contact-value">+61&nbsp; 0491&nbsp; 528&nbsp; 307</span>
    </div>
    <div class="contact-row">
      <span class="contact-label">Email</span>
      <span class="contact-divider"></span>
      <span class="contact-value">dale.pruitt@corvelaxtro.com</span>
    </div>
  </div>
</main>
</body>
</html>
```